CoinLantern one-page corporate website

Our company, CoinLantern is a cryptocurrency Initial Coin Offering ("ICO" marketing and promotion agency, which requires a professional company landing page design whereby prospective clients can learn;
-who we are
-what we do
-what our people are saying about us
-core team members
-subscribe to our mailing list
-how to get in touch (basic contact form)

We are looking for something unique and attractive -- not a standard Vanto template that we could put together ourselves. Plain stock images should not be used. Unique visualizations of the service offerings and creative presentation are key. We are a cutting edge marketing agency and as such, we need to look the part.

Relevant documentation about the business and branding assets have been attached to guide the designer. Certain information will be included by the company at a later date such as team member descriptions. As such, lorem ipsum may be included wherever necessary to help visualize the textual areas.

****Please ensure that you actually utilize the photos and graphics provided so that we can have a good picture of what it would actually look like with our branding.

The site must be responsive HTML CSS Design.

Sites style themes we like for inspiration and specific sections we like ****Very important***:
https://fundrivermesh.com/offers - we like that the token & company logo is used in unique visualizations that connects various ideas together. We imagine unique visuals such as these with our Icon (see attached) serving as a token. We also like the unique and attractive visual theme of the webpage itself.

https://pavoniaholdings.com/ - we like the layout of this website, specifically how the service offerings are displayed in a circular visual graphic with the Pavonia logo in the middle. We imagine a similar type of graphic designed with CoinLantern in the middle.

https://quorvanet.org/ - we like how the logo is central to the theme in this site when you first enter and how it fades + shrinks into the distance as you scroll down.

Target Market(s)

cryptocurrency entrepreneurs and ICOs

Industry/Entity Type

It Company

Coding

Coded - Design and coding required

Number of Pages Required

1 page

Font styles to use
Sans Serif

Colors

Designer to choose colors to be used in the design.

Requirements
Must have
• The site must be responsive HTML CSS Design.
• The page must be modern and visually attractive. Elements must not be static and should have a fluid motion / visual change as the user scrolls through the page.
Should not have
• The project should not use any old stock images or elements which are dull and over-used, but rather images or elements should be unique and well thought out.

```html
<!DOCTYPE html>
<html lang="en">
<head>
<meta charset="utf-8">
<title>CoinLantern</title>
<link href="https://fonts.googleapis.com/css2?family=Mulish:wght@300;400;600;700&display=swap" rel="stylesheet">
<style>
:root{
  --orange:#ff8400;
  --orange-deep:#ff6a00;
  --ink:#222;
  --muted:#777;
  --light:#e9e9e9;
  --night:#0a1330;
  --white:#fff;
  --black:#111;
}
*{box-sizing:border-box;margin:0;padding:0}
html,body{width:1200px;height:3523px;overflow:hidden}
body{font-family:'Mulish',sans-serif;color:var(--ink);background:var(--white);position:relative}
section,header,footer{position:absolute;left:0;width:1200px}
.abs{position:absolute}
.center{text-align:center;left:0;width:1200px}
.section-title{font-weight:400;font-size:28px;letter-spacing:1px;text-transform:uppercase}
.rule{position:absolute;left:560px;width:80px;height:3px;background:#999}

/* hero */
.hero{top:0;height:662px;background:radial-gradient(ellipse at 50% 35%,#1b4d8a 0%,#0e2a5a 35%,var(--night) 75%);overflow:hidden}
.hero-art{position:absolute;inset:0;background:radial-gradient(circle at 48% 30%,rgba(60,190,255,.35),transparent 40%),linear-gradient(180deg,transparent 55%,rgba(20,120,200,.25))}
.logo{left:127px;top:34px;font-size:32px;font-weight:600;color:var(--white)}
.nav{top:46px;font-size:16px;font-weight:600;color:var(--white)}
.hero-kicker{top:258px;font-size:28px;color:var(--white);letter-spacing:1px}
.hero-title{top:304px;font-size:40px;color:var(--white);letter-spacing:1px}
.btn{background:var(--orange);color:var(--white);font-size:18px;text-align:center}
.hero-btn{left:502px;top:369px;width:193px;height:42px;line-height:42px}
.dots{top:612px;left:550px;display:flex;gap:8px}
.dots span{width:14px;height:14px;border-radius:50%;background:var(--white)}
.dots span:first-child{background:transparent;border:2px solid var(--white)}

/* who */
.who{top:662px;height:418px}
.who p{position:absolute;left:216px;width:770px;text-align:center;font-size:13.5px;line-height:26px;color:var(--muted)}

/* what we do */
.what{top:1080px;height:500px;background:var(--orange)}
.what .section-title{color:var(--white)}
.card{position:absolute;text-align:center;color:var(--white)}
.card h3{font-size:21px;font-weight:600;margin-top:16px}
.card .bar{width:60px;height:3px;background:var(--white);margin:10px auto 14px}
.card p{font-size:12.5px;line-height:20px;padding:0 40px}
.card-side{top:1198px;width:310px;height:317px;background:var(--orange-deep);padding-top:60px;top:118px}
.card-left{left:127px;clip-path:polygon(0 4%,100% 0,100% 100%,0 86%)}
.card-right{left:777px;clip-path:polygon(0 0,100% 4%,100% 86%,0 100%)}
.card-mid{left:451px;top:118px;width:312px;height:251px;background:var(--white);color:var(--ink);padding-top:58px;box-shadow:0 8px 14px rgba(0,0,0,.25)}
.card-mid .bar{background:var(--orange)}
.card-mid p{color:#aaa}

/* testimonials */
.quotes{top:1580px;height:491px}
.quotes .sub{top:95px;font-size:24px}
.quote-card{left:272px;top:209px;width:653px;height:216px;background:var(--white);box-shadow:0 4px 22px rgba(0,0,0,.18);text-align:center;padding:50px 60px 0}
.quote-card p{font-style:italic;font-size:14px;line-height:27px;color:var(--muted)}
.quote-card .author{font-size:13px;font-weight:600;margin-top:18px;color:#333}
.avatar{left:565px;top:169px;width:76px;height:76px;border-radius:50%;background:linear-gradient(#c9a58a,#8c7a70);border:3px solid var(--white)}
.qmark{font-size:46px;color:var(--orange);font-weight:700;line-height:1}

/* team */
.team{top:2071px;height:477px;background:var(--light)}
.member{position:absolute;top:129px;width:190px;text-align:center}
.member .photo{width:190px;height:190px}
.member h4{font-size:16px;font-weight:600;margin-top:24px}
.member small{display:block;font-size:9px;line-height:13px;color:var(--muted);margin-top:6px;padding:0 25px}
.social{display:flex;justify-content:center;gap:6px;margin-top:14px}
.social span{width:28px;height:28px;border-radius:50%;border:2px solid var(--orange)}

/* subscribe */
.subscribe{top:2548px;height:378px;background:linear-gradient(120deg,#2b2a28,#161616 50%,#2e2b27)}
.subscribe h2{top:103px;font-size:27px;font-weight:400;color:var(--white)}
.subscribe p{position:absolute;left:380px;width:440px;top:154px;text-align:center;font-size:13px;line-height:26px;color:#555}
.email{left:315px;top:216px;width:436px;height:49px;background:rgba(255,255,255,.18);color:#ddd;font-size:14px;line-height:49px;padding-left:46px}
.sub-btn{left:751px;top:216px;width:153px;height:49px;line-height:49px;font-size:15px;font-weight:700}

/* contact */
.contact{top:2926px;height:455px;background:linear-gradient(90deg,#d7d9d4,#ececec 40%,#e3e3e3)}
.field{position:absolute;background:var(--white);font-size:14px;color:#333;padding:12px 14px}
.submit{left:517px;top:312px;width:180px;height:40px;line-height:40px;font-weight:700;font-size:17px}

/* footer */
.footer{top:3381px;height:142px;background:var(--black);color:#ccc}
.footer .copy{top:36px;font-size:13px}
.foot-social{top:74px;left:514px;display:flex;gap:12px}
.foot-social span{width:40px;height:40px;border-radius:50%;border:2px solid #ddd}
</style>
</head>
<body>

<header class="hero">
  <div class="hero-art" role="img" aria-label="Glowing digital globe with connected hexagon icons on deep blue"></div>
  <div class="abs logo">CoinLantern</div>
  <nav>
    <span class="abs nav" style="left:467px">Who We Are</span>
    <span class="abs nav" style="left:610px">What We Do</span>
    <span class="abs nav" style="left:754px">Testimonials</span>
    <span class="abs nav" style="left:895px">Team</span>
    <span class="abs nav" style="left:977px">Contact Us</span>
  </nav>
  <div class="abs center hero-kicker">ETIAM EU URNA SED PORTA</div>
  <h1 class="abs center hero-title" style="font-weight:400">SUSPENDISSE QUAM LEO MOLESTIE</h1>
  <div class="abs btn hero-btn">Get Started</div>
  <div class="abs dots"><span></span><span></span><span></span><span></span></div>
</header>

<section class="who">
  <h2 class="abs center section-title" style="top:60px">Who We Are</h2>
  <div class="rule" style="top:111px"></div>
  <p style="top:140px">Pellentesque faucibus Ut accumsan ultricies elit Maecenas at justo id velit placerat molestie Donec dictum lectus non odio Cras a ante vitae enim iaculis aliquam Mauris nunc quam venenatis nec euismod sit amet egestas placerat est Pellentesque habitant morbi tristique senectus et netus et malesuada fames ac turpis egestas Cras id elit Integer quis urna Ut ante enim dapibus malesuada fringilla eu condimentum quis tellus</p>
  <p style="top:260px">Etiam eu urna Sed porta Suspendisse quam leo molestie sed luctus quis feugiat in pede Fusce tellus Sed metus augue convallis et vehicula ut pulvinar eu ante Integer arci tellus tristique vitae consequat nec porta vel lectus Nulla sit amet diam Duis non nunc Nulla rhoncus dictum me.</p>
</section>

<section class="what">
  <h2 class="abs center section-title" style="top:40px">What We Do</h2>
  <div class="rule" style="top:88px;background:var(--white)"></div>
  <div class="card card-side card-left">
    <svg width="80" height="70" viewBox="0 0 80 70" fill="none" stroke="#fff" stroke-width="2.5"><circle cx="40" cy="35" r="16"/><path d="M24 35H8M56 35h16M40 19V5M40 51v14M29 24 18 13M51 24l11-11M29 46 18 57M51 46l11 11"/><circle cx="6" cy="35" r="3"/><circle cx="74" cy="35" r="3"/><circle cx="40" cy="3" r="2.5"/><circle cx="40" cy="67" r="2.5"/></svg>
    <h3>Cryptocurrency</h3><div class="bar"></div>
    <p>Morbi diam mauris viverra in gravida eu mattis in ante Morbi eget arcu Morbi porta libero id ullamcorper</p>
  </div>
  <div class="card card-mid">
    <svg width="80" height="60" viewBox="0 0 80 60" fill="none" stroke="#ff8400" stroke-width="3"><path d="M14 24h10l26-14v40L24 36H14z"/><path d="M20 36l6 16h8l-4-15"/><path d="M58 22q6 8 0 16M64 16q12 14 0 28"/></svg>
    <h3>Marketing</h3><div class="bar"></div>
    <p>Morbi diam mauris viverra in gravida eu mattis in ante Morbi eget arcu Morbi porta libero id ullamcorper</p>
  </div>
  <div class="card card-side card-right">
    <svg width="80" height="70" viewBox="0 0 80 70" fill="none" stroke="#fff" stroke-width="2.5"><path d="M40 14a16 16 0 0 0-9 29v7h18v-7a16 16 0 0 0-9-29z"/><path d="M33 56h14M35 62h10M40 2v6M18 12l4 4M62 12l-4 4M10 30h6M64 30h6"/></svg>
    <h3>Knowledge &amp; Idea</h3><div class="bar"></div>
    <p>Morbi diam mauris viverra in gravida eu mattis in ante Morbi eget arcu Morbi porta libero id ullamcorper</p>
  </div>
</section>

<section class="quotes">
  <h2 class="abs center section-title" style="top:62px">What Our People Are</h2>
  <div class="abs center sub">SAYING ABOUT US</div>
  <div class="rule" style="top:138px;background:var(--orange)"></div>
  <div class="abs quote-card">
    <p><span class="qmark" style="font-size:40px;vertical-align:-12px">&ldquo;</span> Morbi diam mauris viverra in gravida eu mattis in ante Morbi eget arcu Morbi porta libero id ullamcorper nonummy nibh ligula pulvinar metus eget consectetuer augue nisi quis lacus Ut ac mi quis lacus mollis aliquam Curabitur <span class="qmark" style="font-size:40px;vertical-align:-22px">&rdquo;</span></p>
    <div style="width:40px;height:2px;background:#999;margin:12px auto 0"></div>
    <div class="author">BY AUTHOR NAME</div>
  </div>
  <div class="abs avatar" role="img" aria-label="Client portrait"></div>
  <svg class="abs" style="left:185px;top:270px" width="30" height="80" viewBox="0 0 30 80" fill="none" stroke="#aaa" stroke-width="2"><path d="M28 2 2 40l26 38"/></svg>
  <svg class="abs" style="left:975px;top:270px" width="30" height="80" viewBox="0 0 30 80" fill="none" stroke="#aaa" stroke-width="2"><path d="M2 2l26 38L2 78"/></svg>
</section>

<section class="team">
  <h2 class="abs center section-title" style="top:50px">Core Team Members</h2>
  <div class="rule" style="top:95px;width:60px;left:570px"></div>
  <svg class="abs" style="left:110px;top:200px" width="26" height="64" viewBox="0 0 26 64" fill="none" stroke="#aaa" stroke-width="2"><path d="M24 2 2 32l22 30"/></svg>
  <svg class="abs" style="left:1092px;top:200px" width="26" height="64" viewBox="0 0 26 64" fill="none" stroke="#aaa" stroke-width="2"><path d="M2 2l22 30L2 62"/></svg>
  <div class="member" style="left:176px"><div class="photo" role="img" aria-label="Team member portrait" style="background:linear-gradient(#b59b86,#7a5a46)"></div><h4>Member Name</h4><small>Class aptent taciti sociosqu ad litora torquent per conubia</small><div class="social"><span></span><span></span><span></span></div></div>
  <div class="member" style="left:406px"><div class="photo" role="img" aria-label="Team member portrait" style="background:linear-gradient(#e2e0dc,#b99a86)"></div><h4>Member Name</h4><small>Class aptent taciti sociosqu ad litora torquent per conubia</small><div class="social"><span></span><span></span><span></span></div></div>
  <div class="member" style="left:634px"><div class="photo" role="img" aria-label="Team member portrait" style="background:linear-gradient(#cfcbc5,#8f857b)"></div><h4>Member Name</h4><small>Class aptent taciti sociosqu ad litora torquent per conubia</small><div class="social"><span></span><span></span><span></span></div></div>
  <div class="member" style="left:862px"><div class="photo" role="img" aria-label="Team member portrait" style="background:linear-gradient(#8a8580,#4c4642)"></div><h4>Member Name</h4><small>Class aptent taciti sociosqu ad litora torquent per conubia</small><div class="social"><span></span><span></span><span></span></div></div>
</section>

<section class="subscribe" role="img" aria-label="Dim desk scene with laptop and notebook behind the mailing list form">
  <h2 class="abs center">SUBSCRIBE TO OUR MAILING LIST</h2>
  <p>Etiam eu urna Sed porta Suspendisse quam leo molestie sed luctus quis feugiat in pede Fusce tellus Sed metus augue convallis et vehicula ut pulvinar eu ante Integer</p>
  <div class="abs email">Email address</div>
  <svg class="abs" style="left:330px;top:233px" width="20" height="15" viewBox="0 0 20 15" fill="none" stroke="#ccc" stroke-width="1.5"><rect x="1" y="1" width="18" height="13"/><path d="M1 1l9 7 9-7"/></svg>
  <div class="abs btn sub-btn">SUBSCRIBE</div>
</section>

<section class="contact" role="img" aria-label="Bright desk with plant and keyboard behind the contact form">
  <h2 class="abs center section-title" style="top:66px">Get In Touch</h2>
  <div class="rule" style="top:108px;background:#555"></div>
  <div class="field" style="left:193px;top:140px;width:408px;height:47px">Name</div>
  <div class="field" style="left:193px;top:192px;width:408px;height:47px">Email</div>
  <div class="field" style="left:193px;top:246px;width:408px;height:45px">Phone</div>
  <div class="field" style="left:608px;top:140px;width:406px;height:151px">Message</div>
  <div class="abs btn submit">SUBMIT</div>
</section>

<footer class="footer">
  <div class="abs center copy">&copy; 2017 Company Name &nbsp;All right reserved &nbsp;Term of Use</div>
  <div class="abs foot-social"><span></span><span></span><span></span><span></span></div>
</footer>

</body>
</html>
```